Honigetikett gesucht
Zielgruppe
Ich bin ein Hobbyimker und brauche ein Etikett für meinen Honig. Zielgruppe = Jeder
Aufgabenstellung
Bitte keine schwarzen Etiketten mehr... gefällt uns leider nicht. Danke!
Das Etikett ist für Honig, 500 Gramm Glas. Man muss den gesetzlichen Vorgaben einhalten. https://www.wabenhof-vorlu.at/de/labor/lebensmittelrecht.html
Blütenhonig aus Österreich
Name
Adresse
500 g
Trocken und vor Licht und Wärme geschützt lagern.
Mindestens haltbar bis:
Sichtfeldregelung
Sachbezeichnung und Nettofüllmenge müssen am Etikett in einem Sichtfeld angebracht werden. Ein Sichtfeld ist eine Oberfläche einer Verpackung, die von einem einzigen Blickpunkt aus gelesen werden kann.
Mindesthaltbarkeitsdatum und Lagerbedingungen sind in einem Sichtfeld anzubringen. Dabei muss die Lagerbedingung über oder unter der Haltbarkeit angeführt werden und darf nicht durch Bild- oder Schrift getrennt sein.
Mindestschriftgröße aller verpflichtenden Angaben (Ausnahme Nettofüllmenge) Mindestschriftgröße:
Die verwendete Schrift muss am kleinen „x“ der verwendeten Schriftart gemessen mindestens 1,2mm Höhe ausmachen
Erreicht die Gesamtoberfläche des Gebindes auf dem Ein Etikett angebracht werden kann max. 80cm2, so muss die Höhe am kleinen „x“ der verwendeten Schriftart gemessen mindestens 0,9mm Höhe ausmachen (beim Honigglas wäre dies erst unter dem 125g Glas)
Die Mindestschriftgröße der Nettofüllmenge bleibt davon unberührt und unterliegt weiterhin der Fertigpackungsverordnung (siehe Nettofüllmenge)

```html
<!DOCTYPE html>
<html lang="de">
<head>
<meta charset="utf-8">
<title>Blütenhonig – Etikett</title>
<link rel="stylesheet" href="https://fonts.googleapis.com/css2?family=Amatic+SC:wght@700&family=Montserrat:wght@400;500;700&display=swap">
<style>
  :root {
    --page: #ffffff;
    --label-paper: #e6e2dc;
    --ink: #2c2c2c;
    --hex-fill: #878787;
    --hex-line: #8e8e8e;
  }
  html, body {
    margin: 0;
    padding: 0;
    width: 1200px;
    height: 1200px;
    overflow: hidden;
    background: var(--page);
  }
  .canvas {
    position: relative;
    width: 1200px;
    height: 1200px;
  }
  .label {
    position: absolute;
    left: 51px;
    top: 352px;
    width: 1101px;
    height: 497px;
    overflow: hidden;
  }
  .floral-backdrop {
    position: absolute;
    inset: 0;
    background: radial-gradient(ellipse at 50% 50%, #e8e4de 0%, var(--label-paper) 70%, #e1ddd6 100%);
  }
  .honeycomb {
    position: absolute;
    inset: 0;
    width: 1101px;
    height: 497px;
  }
  .hex-solid { fill: var(--hex-fill); }
  .hex-outline { fill: none; stroke: var(--hex-line); stroke-width: 3.5; }

  .text {
    position: absolute;
    color: var(--ink);
    font-family: "Montserrat", sans-serif;
    margin: 0;
    line-height: 1;
    white-space: nowrap;
  }
  .product-name {
    left: 0;
    width: 1101px;
    top: 170px;
    text-align: center;
    font-family: "Amatic SC", cursive;
    font-weight: 700;
    font-size: 112px;
    letter-spacing: 1px;
  }
  .origin {
    left: 0;
    width: 1101px;
    top: 281px;
    text-align: center;
    font-size: 37px;
    font-weight: 400;
  }
  .net-quantity {
    left: 0;
    width: 1101px;
    top: 375px;
    text-align: center;
    font-size: 37px;
    font-weight: 400;
  }
  .net-quantity .estimated-sign { font-weight: 700; margin-right: 14px; }
  .best-before {
    left: 50px;
    top: 279px;
    font-size: 16px;
    line-height: 19px;
  }
  .best-before strong { font-weight: 700; }
  .storage {
    left: 50px;
    top: 328px;
    font-size: 11px;
    line-height: 14px;
    font-weight: 500;
  }
  .producer {
    left: 50px;
    top: 396px;
    font-size: 16px;
    line-height: 19.5px;
  }
</style>
</head>
<body>
<div class="canvas">
  <div class="label">
    <div class="floral-backdrop" role="img" aria-label="Zarte, hell gezeichnete Blüten und Blätter als Hintergrundmuster auf beigem Papier"></div>

    <svg class="honeycomb" viewBox="60 415 1297 585" aria-hidden="true">
      <!-- left cluster -->
      <polygon class="hex-solid" points="235,432 272.5,367 347.5,367 385,432 347.5,497 272.5,497"/>
      <polygon class="hex-outline" points="100,511 137.5,446 212.5,446 250,511 212.5,576 137.5,576"/>
      <polygon class="hex-outline" points="233,586 270.5,521 345.5,521 383,586 345.5,651 270.5,651"/>
      <!-- right cluster -->
      <polygon class="hex-outline" points="1144,495 1181.5,430 1256.5,430 1294,495 1256.5,560 1181.5,560"/>
      <polygon class="hex-solid" points="1143,648 1180.5,583 1255.5,583 1293,648 1255.5,713 1180.5,713"/>
      <polygon class="hex-outline" points="1277,722 1314.5,657 1389.5,657 1427,722 1389.5,787 1314.5,787"/>
      <polygon class="hex-outline" points="1144,801 1181.5,736 1256.5,736 1294,801 1256.5,866 1181.5,866"/>
      <polygon class="hex-solid" points="1014,871 1051.5,806 1126.5,806 1164,871 1126.5,936 1051.5,936"/>
      <polygon class="hex-outline" points="1277,875 1314.5,810 1389.5,810 1427,875 1389.5,940 1314.5,940"/>
      <polygon class="hex-outline" points="1012,1020 1049.5,955 1124.5,955 1162,1020 1124.5,1085 1049.5,1085"/>
    </svg>

    <h1 class="text product-name">Blütenhonig</h1>
    <p class="text origin">aus Österreich</p>
    <p class="text net-quantity"><span class="estimated-sign">℮</span>500g</p>

    <p class="text best-before">Mindestens haltbar<br>bis: <strong>09/2023</strong></p>
    <p class="text storage">Trocken und vor Licht und<br>Wärme geschützt lagern.</p>

    <address class="text producer" style="font-style: normal;">Selma Kranvik<br>Quittenweg 7c<br>1220 Wien</address>
  </div>
</div>
</body>
</html>
```